Quenby Loans - Mortgage Brokers Australia

redesign of quenbyloans.com.au website. We are a mortgage brokering service and are clients are based in Australia. The demographics are 30-45 year holds looking to borrow money to purchase, invest and refinance property.

Please research other lending websites in Australia. My favourites are:

https://www.borvix.com.au/
https://www.tallowridgehomes.com.au/

I want CTA's on the first page. For Refinance/Purchase.

I DO NOT WANT ANYONE TO TRY AND CONTACT ME VIA EMAIL/What's app

My current website is: https/www.quenbyloans.com.au/home and the password is "Wrpk8157#"

Target Market(s)

30-45 year hold professionals, first home buyers

Industry/Entity Type

Mortgage Brokerage

Number of Pages Required

4 page

Font styles to use
Sans Serif

Colors
e34197
6b449b
ffc214
0792cd
34a7d8

Requirements
Must have
• Must be fresh, clean and professional - with a beautiful hero section

```html
<!DOCTYPE html>
<html lang="en">
<head>
<meta charset="utf-8">
<title>Quenby Loans – Mortgage Brokers Australia</title>
<link href="https://fonts.googleapis.com/css2?family=Poppins:wght@300;400;500;600;700&display=swap" rel="stylesheet">
<style>
:root{
  --pink:#e34197;
  --purple:#6b449b;
  --purple-soft:#7b5ea7;
  --purple-deep:#4e3a79;
  --yellow:#ffc214;
  --blue:#0792cd;
  --blue-light:#34a7d8;
  --lavender:#efecf6;
  --ink:#2b2540;
  --grey-text:#5a5568;
  --panel:#f1f1f3;
  --white:#ffffff;
}
*{box-sizing:border-box;margin:0;padding:0}
html,body{width:1200px;height:3639px;overflow:hidden}
body{font-family:"Poppins",sans-serif;color:var(--ink);background:var(--white);position:relative}
a{text-decoration:none;color:inherit}

/* hero */
.hero{position:absolute;left:0;top:0;width:1200px;height:638px;background:var(--lavender);overflow:hidden}
.hero-shape{position:absolute;left:0;top:0}
.brand{position:absolute;left:150px;top:42px;display:flex;align-items:center;gap:10px;font-size:27px;font-weight:600;color:var(--pink)}
.brand-dot{width:14px;height:14px;border-radius:50%;background:var(--yellow)}
.nav{position:absolute;left:488px;top:42px;display:flex;gap:29px;font-size:14px;font-weight:500;color:var(--white);letter-spacing:.2px}
.hero-title{position:absolute;left:150px;top:236px;font-size:28px;line-height:45px;font-weight:400;color:var(--ink)}
.hero-title strong{font-weight:600;color:var(--purple);font-size:33px}
.btn{position:absolute;display:flex;align-items:center;justify-content:center;gap:14px;border-radius:24px;color:var(--white);font-size:15px;font-weight:500;box-shadow:0 6px 14px rgba(107,68,155,.3)}
.btn svg{width:24px;height:10px}
.btn-pink{background:var(--pink)}
.btn-purple{background:var(--purple)}
.hero-art{position:absolute;left:560px;top:150px}
.mouse{position:absolute;left:591px;top:557px;width:18px;height:30px;border:2px solid #9a90b3;border-radius:10px}
.mouse::after{content:"";position:absolute;left:6px;top:5px;width:2px;height:6px;background:#9a90b3;border-radius:1px}

/* partners */
.partners{position:absolute;left:124px;top:688px;width:953px;height:55px;display:flex;justify-content:space-between;align-items:center}
.partner{display:flex;align-items:center;gap:8px;font-size:18px;font-weight:600;color:var(--purple-deep)}
.partner i{display:block;width:14px;height:14px;border-radius:3px;background:var(--blue)}
.rule{position:absolute;left:124px;top:775px;width:953px;height:1px;background:#d8d6de}

/* intro */
.section-title{position:absolute;left:0;width:1200px;text-align:center;font-size:29px;font-weight:600;color:var(--purple)}
.intro-text{position:absolute;left:0;top:890px;width:1200px;text-align:center;font-size:13px;line-height:25px;color:var(--grey-text)}
.feature{position:absolute;left:155px;width:420px;display:flex;gap:30px}
.feature-icon{flex:none;width:76px;height:76px;border-radius:50%;border:2px dashed #b8a9d4;display:flex;align-items:center;justify-content:center}
.feature-icon span{width:44px;height:44px;border-radius:10px;background:linear-gradient(135deg,var(--purple),var(--pink))}
.feature h3{font-size:15px;font-weight:500;color:var(--ink);margin:2px 0 12px}
.feature p{font-size:13px;line-height:20px;color:var(--grey-text)}
.keys-photo{position:absolute;left:600px;top:991px;width:450px;height:411px;background:linear-gradient(145deg,#8a7a62,#5c4e3e 60%,#3b3128)}

/* services */
.services{position:absolute;left:0;top:1515px;width:1200px;height:690px}
.services-bg{position:absolute;left:0;top:0}
.services-title{position:absolute;left:0;top:130px;width:1200px;text-align:center;font-size:29px;font-weight:600;color:var(--white)}
.services-line{position:absolute;left:566px;top:181px;width:68px;height:3px;background:var(--white);border-radius:2px}
.card{position:absolute;top:233px;width:267px;height:356px;background:var(--white);border-radius:6px 50px 6px 50px;text-align:center;padding-top:40px}
.card-icon{width:110px;height:110px;margin:0 auto 22px;border-radius:50%;border:3px solid var(--purple);display:flex;align-items:center;justify-content:center}
.card-icon span{width:46px;height:46px;border-radius:8px;border:3px solid var(--pink)}
.card h3{font-size:20px;font-weight:600;color:var(--purple);margin-bottom:14px}
.card p{font-size:12px;line-height:21px;color:var(--grey-text);padding:0 22px}
.card-btn{display:inline-flex;align-items:center;gap:10px;margin-top:22px;padding:0 20px;height:36px;border:2px solid var(--purple-deep);border-radius:18px;font-size:13px;color:var(--ink)}
.card-btn svg{width:12px;height:8px}
.card.featured{background:var(--pink);border-radius:50px 6px 50px 6px}
.card.featured .card-icon{border-color:var(--white)}
.card.featured .card-icon span{border-color:var(--white)}
.card.featured h3,.card.featured p{color:var(--white)}
.card.featured .card-btn{background:var(--white);border-color:var(--white);color:var(--pink)}

/* news */
.news-card{position:absolute;top:2280px;width:278px;height:366px;background:var(--white);box-shadow:0 4px 14px rgba(0,0,0,.07)}
.news-photo{width:278px;height:248px}
.news-meta{display:flex;align-items:center;gap:6px;margin:22px 18px 12px;font-size:11px;color:var(--grey-text)}
.news-meta svg{width:11px;height:11px}
.news-card h4{margin:0 18px;font-size:13px;line-height:21px;font-weight:400;color:var(--ink)}
.slider-arrow{position:absolute;top:2414px;width:32px;height:32px;border-radius:50%;background:#e4e0ee;display:flex;align-items:center;justify-content:center}
.slider-arrow svg{width:10px;height:10px}
.news-next{position:absolute;left:583px;top:2628px;width:36px;height:36px;border-radius:50%;background:var(--purple);display:flex;align-items:center;justify-content:center}

/* about */
.about{position:absolute;left:0;top:2732px;width:1200px;height:526px;background:var(--panel);overflow:hidden}
.about-photo{position:absolute;left:140px;top:58px;width:390px;height:390px;border-radius:50%;background:radial-gradient(circle at 55% 45%,#b48b63,#6f5a4a 45%,#3b4a66 80%)}
.eyebrow{position:absolute;left:621px;top:108px;font-size:12px;font-weight:600;color:var(--ink);letter-spacing:.3px}
.about h2{position:absolute;left:621px;top:140px;font-size:30px;line-height:40px;font-weight:600;color:var(--ink)}
.about p{position:absolute;left:621px;top:250px;width:425px;font-size:14px;line-height:26px;color:var(--grey-text)}

/* footer */
.footer-brand{position:absolute;left:205px;top:3330px;display:flex;align-items:center;gap:10px;font-size:27px;font-weight:600;color:var(--pink)}
.contact-line{position:absolute;left:203px;display:flex;gap:14px;font-size:13px;line-height:19px;color:var(--ink)}
.contact-line svg{flex:none;width:15px;height:17px;margin-top:2px}
.footer-head{position:absolute;font-size:16px;font-weight:600;color:var(--ink)}
.footer-links{position:absolute;left:491px;top:3364px;list-style:none;font-size:12.5px;line-height:25.5px;color:var(--ink)}
.footer-links li{display:flex;align-items:center;gap:8px}
.footer-links svg{width:6px;height:9px}
.subscribe{position:absolute;left:694px;top:3370px;width:308px;height:38px;display:flex;border:1px solid #bdb7ca;border-radius:19px;overflow:hidden}
.subscribe span{flex:1;padding-left:22px;line-height:36px;font-size:13px;color:var(--grey-text)}
.subscribe b{width:104px;background:var(--purple);color:var(--white);font-weight:400;font-size:14px;text-align:center;line-height:36px}
.social{position:absolute;top:3471px;width:38px;height:38px;border-radius:50%;background:var(--purple)}
.footer-rule{position:absolute;left:0;top:3570px;width:1200px;height:1px;background:#dcd9e2}
.legal{position:absolute;top:3596px;font-size:12px;color:var(--ink)}
</style>
</head>
<body>

<header class="hero">
  <svg class="hero-shape" width="1200" height="638" viewBox="0 0 1200 638">
    <path d="M405 0 C440 105 540 150 640 165 C710 175 725 300 705 410 C690 520 760 600 800 638 L1200 638 L1200 0 Z" fill="var(--purple-soft)"/>
    <circle cx="85" cy="420" r="11" fill="#dcd6ea"/>
    <circle cx="52" cy="495" r="22" fill="#dcd6ea"/>
  </svg>
  <div class="brand"><span class="brand-dot"></span>Quenby Loans</div>
  <nav class="nav">
    <a>HOME</a><a>SERVICES</a><a>ABOUT US</a><a>WHY USE BROKER</a><a>BLOG</a><a>CONTACT US</a>
  </nav>
  <h1 class="hero-title">We are passionate about<br>helping you <strong>Achieve<br>your financial goals!</strong></h1>
  <a class="btn btn-pink" style="left:150px;top:413px;width:157px;height:42px">Refinance
    <svg viewBox="0 0 24 10"><path d="M0 5H22M17 1L22 5L17 9" stroke="#fff" stroke-width="1.4" fill="none"/></svg></a>
  <a class="btn btn-purple" style="left:320px;top:413px;width:158px;height:42px">Purchase
    <svg viewBox="0 0 24 10"><path d="M0 5H22M17 1L22 5L17 9" stroke="#fff" stroke-width="1.4" fill="none"/></svg></a>
  <svg class="hero-art" width="540" height="420" viewBox="0 0 540 420" role="img" aria-label="Illustration of a family of four standing beside their new house">
    <defs><linearGradient id="heroFill" x1="0" y1="0" x2="1" y2="1">
      <stop offset="0" stop-color="#ffffff"/><stop offset="1" stop-color="#e2d8f0"/></linearGradient></defs>
    <path d="M60 120 C70 40 150 5 230 20 C300 32 330 60 400 45 C470 30 530 80 520 160 C512 230 535 300 490 350 C440 405 330 400 250 395 C170 390 80 400 40 340 C5 285 50 200 60 120 Z" fill="url(#heroFill)"/>
  </svg>
  <div class="mouse"></div>
</header>

<div class="partners">
  <div class="partner"><i></i>Harlow Bank</div>
  <div class="partner" style="font-size:14px"><i></i>Kestrel Finance</div>
  <div class="partner" style="font-size:24px">Marlo</div>
  <div class="partner"><i style="background:var(--pink)"></i>Tidewell Bank</div>
  <div class="partner" style="font-size:26px;font-weight:400;color:var(--blue)">Corvanta</div>
  <div class="partner" style="font-size:22px;font-weight:400">brightlend</div>
</div>
<div class="rule"></div>

<h2 class="section-title" style="top:836px">The new way to get your mortage</h2>
<p class="intro-text">Quenby Loans manage the entire process for you from start to finish and as every one of our clients is different,<br>we fully assess your individual situation and provide a solution to meet your particular needs.</p>

<div class="feature" style="top:1006px">
  <div class="feature-icon"><span></span></div>
  <div><h3>We work for you, not the lenders</h3><p>Choosing the right home loan is like finding<br>the right match, but you need more.</p></div>
</div>
<div class="feature" style="top:1127px">
  <div class="feature-icon"><span></span></div>
  <div><h3>We'll find you the perfect match</h3><p>We're all about helping you reach your next<br>financial goal</p></div>
</div>
<div class="feature" style="top:1243px">
  <div class="feature-icon"><span></span></div>
  <div><h3>We Are Fully Dedicated To Support You</h3><p>We assess &amp; tailor your mortgage to suit your<br>financial situation</p></div>
</div>
<a class="btn btn-purple" style="left:262px;top:1352px;width:158px;height:42px">Book Now
  <svg viewBox="0 0 24 10"><path d="M0 5H22M17 1L22 5L17 9" stroke="#fff" stroke-width="1.4" fill="none"/></svg></a>
<div class="keys-photo" role="img" aria-label="Photo of a hand holding house keys over a floor plan"></div>

<section class="services">
  <svg class="services-bg" width="1200" height="690" viewBox="0 0 1200 690">
    <defs><linearGradient id="band" x1="0" y1="0" x2="1" y2="1">
      <stop offset="0" stop-color="#5e4590"/><stop offset="1" stop-color="#6f5aa0"/></linearGradient></defs>
    <path d="M0 100 L600 0 L1200 100 L1200 690 L0 690 Z" fill="var(--yellow)"/>
    <path d="M0 112 L600 12 L1200 112 L1200 690 L0 690 Z" fill="url(#band)" role="img" aria-label="Faded photo of a couple planning their finances"/>
  </svg>
  <h2 class="services-title">What Can Quenby Loans Do for You?</h2>
  <div class="services-line"></div>
  <div class="card" style="left:150px">
    <div class="card-icon"><span></span></div>
    <h3>Home Loans</h3>
    <p>Your home loan is likely to be<br>one of your life's biggest...</p>
    <a class="card-btn">Learn More <svg viewBox="0 0 12 8"><path d="M0 4H10M7 1L10 4L7 7" stroke="currentColor" fill="none"/></svg></a>
  </div>
  <div class="card featured" style="left:467px">
    <div class="card-icon"><span></span></div>
    <h3>Refinance</h3>
    <p>Refinancing refers to the process<br>of paying out your current...</p>
    <a class="card-btn">Learn More <svg viewBox="0 0 12 8"><path d="M0 4H10M7 1L10 4L7 7" stroke="currentColor" fill="none"/></svg></a>
  </div>
  <div class="card" style="left:783px">
    <div class="card-icon"><span></span></div>
    <h3>Investment Loans</h3>
    <p>Your home loan is likely to be<br>one of your life's biggest...</p>
    <a class="card-btn">Learn More <svg viewBox="0 0 12 8"><path d="M0 4H10M7 1L10 4L7 7" stroke="currentColor" fill="none"/></svg></a>
  </div>
</section>

<div class="slider-arrow" style="left:102px"><svg viewBox="0 0 10 10"><path d="M6 2L3 5L6 8" stroke="var(--purple)" fill="none" stroke-width="1.3"/></svg></div>
<div class="slider-arrow" style="left:1069px"><svg viewBox="0 0 10 10"><path d="M4 2L7 5L4 8" stroke="var(--purple)" fill="none" stroke-width="1.3"/></svg></div>

<article class="news-card" style="left:150px">
  <div class="news-photo" role="img" aria-label="Photo of a café worker packing takeaway orders" style="background:linear-gradient(150deg,#c9cfd6,#8c7a66 60%,#4a4d58)"></div>
  <div class="news-meta"><svg viewBox="0 0 12 12"><circle cx="6" cy="6" r="5" stroke="#555" fill="none"/><path d="M6 3V6H8" stroke="#555" fill="none"/></svg>13 Jun, 2018</div>
  <h4>Flow of credit to small businesses remains strong</h4>
</article>
<article class="news-card" style="left:461px">
  <div class="news-photo" role="img" aria-label="Photo of a shop owner standing in a blue doorway" style="background:linear-gradient(150deg,#2d6a8a,#3f7f9c 45%,#d9d6d0)"></div>
  <div class="news-meta"><svg viewBox="0 0 12 12"><circle cx="6" cy="6" r="5" stroke="#555" fill="none"/><path d="M6 3V6H8" stroke="#555" fill="none"/></svg>13 Jun, 2018</div>
  <h4>WageBridge 2.0 is about to begin: here's what you need to know</h4>
</article>
<article class="news-card" style="left:772px">
  <div class="news-photo" role="img" aria-label="Aerial photo of a coastal suburb" style="background:linear-gradient(150deg,#1f4d6b,#4d6a72 45%,#a08e78)"></div>
  <div class="news-meta"><svg viewBox="0 0 12 12"><circle cx="6" cy="6" r="5" stroke="#555" fill="none"/><path d="M6 3V6H8" stroke="#555" fill="none"/></svg>13 Jun, 2018</div>
  <h4>Is now a good time to buy property? Two-thirds of investors say 'yes'</h4>
</article>
<div class="news-next"><svg width="10" height="10" viewBox="0 0 10 10"><path d="M4 2L7 5L4 8" stroke="#fff" fill="none" stroke-width="1.4"/></svg></div>

<section class="about">
  <div class="about-photo" role="img" aria-label="Photo of cupped hands holding a small wooden house"></div>
  <div class="eyebrow">ABOUT COMPANY</div>
  <h2>We Focus on your needs,<br>not the banks</h2>
  <p>It is far too often that you hear of people ending up with the wrong type of loan, a bad deal, or sign up with promises that are never kept. Well, I am in the business of making sure that never happens to you.</p>
  <a class="btn btn-purple" style="left:622px;top:370px;width:158px;height:40px">Learn More
    <svg viewBox="0 0 24 10"><path d="M0 5H22M17 1L22 5L17 9" stroke="#fff" stroke-width="1.4" fill="none"/></svg></a>
</section>

<footer>
  <div class="footer-brand"><span class="brand-dot"></span>Quenby Loans</div>
  <div class="contact-line" style="top:3422px">
    <svg viewBox="0 0 15 17"><path d="M7.5 16C7.5 16 1.5 10 1.5 6.5A6 6 0 0 1 13.5 6.5C13.5 10 7.5 16 7.5 16Z" fill="var(--ink)"/><circle cx="7.5" cy="6.5" r="2.2" fill="#fff"/></svg>
    <span>42 Wattle Lane<br>Carindale QLD 4152</span>
  </div>
  <div class="contact-line" style="top:3481px;font-size:16px;color:var(--purple)">
    <svg viewBox="0 0 15 17"><path d="M3 1L6 4L4.5 6.5C5.5 9 7.5 11 10 12L12 10.5L14.5 13.5L12.5 16C6.5 15 1.5 9 1 3Z" fill="var(--ink)"/></svg>
    <span>(07) 3100 2468</span>
  </div>

  <div class="footer-head" style="left:491px;top:3326px">COMPANY</div>
  <ul class="footer-links">
    <li><svg viewBox="0 0 6 9"><path d="M1 1L5 4.5L1 8" stroke="#333" fill="none"/></svg>Home</li>
    <li><svg viewBox="0 0 6 9"><path d="M1 1L5 4.5L1 8" stroke="#333" fill="none"/></svg>Services</li>
    <li><svg viewBox="0 0 6 9"><path d="M1 1L5 4.5L1 8" stroke="#333" fill="none"/></svg>About Us</li>
    <li><svg viewBox="0 0 6 9"><path d="M1 1L5 4.5L1 8" stroke="#333" fill="none"/></svg>Why Use Broker</li>
    <li><svg viewBox="0 0 6 9"><path d="M1 1L5 4.5L1 8" stroke="#333" fill="none"/></svg>Blog</li>
    <li><svg viewBox="0 0 6 9"><path d="M1 1L5 4.5L1 8" stroke="#333" fill="none"/></svg>Contact Us</li>
  </ul>

  <div class="footer-head" style="left:701px;top:3326px">SUBSCRIBE</div>
  <div class="subscribe"><span>Email address</span><b>Subscribe</b></div>
  <div class="footer-head" style="left:701px;top:3436px">FOLLOW US</div>
  <div class="social" style="left:701px"></div>
  <div class="social" style="left:753px"></div>

  <div class="footer-rule"></div>
  <div class="legal" style="left:205px">© 2021 Quenby Loans. All Rights Reserved.</div>
  <div class="legal" style="left:855px">Privacy Policy &nbsp;|&nbsp; Terms of Use</div>
</footer>

</body>
</html>
```